Opening a Hair Salon

Looking for a design for my sign that looks high end, an emphasis on color but welcoming to men and women.

The name is Norvale Haircuts and Colors

Trying capture a more affluent client. Looking for a very modern look.

Reason: Time is going to quick and would like to see a few more options.

Hair

```html
<!DOCTYPE html>
<html lang="en">
<head>
<meta charset="utf-8">
<title>Norvale Haircuts and Colors – Sign Options</title>
<link rel="stylesheet" href="https://fonts.googleapis.com/css2?family=Jost:wght@500;600;700&display=swap">
<style>
  :root {
    --ink: #16124a;
    --cut-red: #ff1a1a;
    --paper: #ffffff;
  }
  * { box-sizing: border-box; margin: 0; padding: 0; }
  html, body {
    width: 1200px;
    height: 1000px;
    overflow: hidden;
    background: var(--paper);
  }
  .canvas {
    position: relative;
    width: 1200px;
    height: 1000px;
    background: var(--paper);
    font-family: "Jost", "Futura", sans-serif;
    color: var(--ink);
  }
  .sign-strip {
    position: absolute;
    border: 2px dashed var(--cut-red);
    transform-origin: center center;
  }
  .sign-strip--compact {
    left: 216px; top: 216px;
    width: 757px; height: 190px;
    transform: rotate(-6deg);
  }
  .sign-strip--wide {
    left: 232px; top: 681px;
    width: 872px; height: 175px;
    transform: rotate(3.4deg);
  }
  .brand {
    position: absolute;
    display: flex;
    flex-direction: column;
    font-weight: 600;
    color: var(--ink);
  }
  .brand__mark {
    display: inline-block;
    border-radius: 50%;
    background: var(--ink);
    margin-right: 12px;
    vertical-align: middle;
  }
  .brand__name { line-height: 1; letter-spacing: 0.5px; }
  .brand__tagline { line-height: 1; letter-spacing: 0.3px; text-transform: uppercase; }

  .sign-strip--compact .brand { left: 160px; top: 38px; }
  .sign-strip--compact .brand__name { font-size: 60px; }
  .sign-strip--compact .brand__mark { width: 18px; height: 18px; }
  .sign-strip--compact .brand__tagline { font-size: 21px; margin-top: 10px; margin-left: 46px; }

  .sign-strip--wide .brand { left: 120px; top: 24px; }
  .sign-strip--wide .brand__name { font-size: 64px; }
  .sign-strip--wide .brand__mark { width: 20px; height: 20px; }
  .sign-strip--wide .brand__tagline { font-size: 33px; margin-top: 16px; margin-left: 96px; }

  .phone {
    position: absolute;
    display: flex;
    align-items: center;
    gap: 10px;
    font-weight: 700;
    white-space: nowrap;
  }
  .phone svg { fill: var(--ink); }
  .sign-strip--compact .phone { left: 486px; top: 118px; font-size: 33px; }
  .sign-strip--compact .phone svg { width: 40px; height: 32px; }
  .sign-strip--wide .phone { left: 630px; top: 40px; font-size: 29px; }
  .sign-strip--wide .phone svg { width: 38px; height: 28px; }

  .cut-icon {
    position: absolute;
    width: 110px;
    height: 60px;
  }
  .cut-icon--top { left: 946px; top: 106px; transform: rotate(-22deg); }
  .cut-icon--bottom { left: 140px; top: 590px; transform: scaleX(-1) rotate(-22deg); }
  .cut-icon path, .cut-icon ellipse { stroke: var(--cut-red); }
</style>
</head>
<body>
<main class="canvas">

  <svg class="cut-icon cut-icon--top" viewBox="0 0 110 60" aria-hidden="true">
    <path d="M4 50 L70 24" stroke-width="5" fill="none"/>
    <path d="M4 50 L72 38" stroke-width="5" fill="none"/>
    <ellipse cx="84" cy="18" rx="13" ry="9" fill="none" stroke-width="3"/>
    <ellipse cx="90" cy="42" rx="14" ry="9" fill="none" stroke-width="3"/>
  </svg>

  <section class="sign-strip sign-strip--compact" aria-label="Sign option one">
    <div class="brand">
      <span class="brand__name"><span class="brand__mark"></span>Norvale</span>
      <span class="brand__tagline">Haircuts &amp; Colors</span>
    </div>
    <div class="phone">
      <svg viewBox="0 0 40 32" aria-hidden="true">
        <path d="M2 10 C6 2 34 2 38 10 L38 13 L30 13 L29 9 L11 9 L10 13 L2 13 Z"/>
        <path d="M9 15 L31 15 L37 30 L3 30 Z"/>
      </svg>
      <span>1234 5678</span>
    </div>
  </section>

  <svg class="cut-icon cut-icon--bottom" viewBox="0 0 110 60" aria-hidden="true">
    <path d="M4 50 L70 24" stroke-width="5" fill="none"/>
    <path d="M4 50 L72 38" stroke-width="5" fill="none"/>
    <ellipse cx="84" cy="18" rx="13" ry="9" fill="none" stroke-width="3"/>
    <ellipse cx="90" cy="42" rx="14" ry="9" fill="none" stroke-width="3"/>
  </svg>

  <section class="sign-strip sign-strip--wide" aria-label="Sign option two">
    <div class="brand">
      <span class="brand__name"><span class="brand__mark"></span>Norvale</span>
      <span class="brand__tagline">Haircuts &amp; Colors</span>
    </div>
    <div class="phone">
      <svg viewBox="0 0 40 32" aria-hidden="true">
        <path d="M2 10 C6 2 34 2 38 10 L38 13 L30 13 L29 9 L11 9 L10 13 L2 13 Z"/>
        <path d="M9 15 L31 15 L37 30 L3 30 Z"/>
      </svg>
      <span>1234 5678</span>
    </div>
  </section>

</main>
</body>
</html>
```